Brightnest Stays Stationery Design

Letterpaper, business cards, notebook, envelope A4 & A5

Target Market(s)

Business, accommodation, hotels, flexible housing

Font styles to use
Other font styles liked:
• Montserrat

Colors

Designer to choose only greyscale colors for use in the design.

Requirements
Must have
• Luxurious appearance
Keep it simple, just like the logo
Modern
Nice to have
• Tight Luxury Design
Should not have
• Illustrations
Decorative

```html
<!DOCTYPE html>
<html lang="en">
<head>
<meta charset="utf-8">
<title>Brightnest Stays Stationery</title>
<link href="https://fonts.googleapis.com/css2?family=Montserrat:wght@400&family=Open+Sans:wght@400;600&display=swap" rel="stylesheet">
<style>
:root{
  --bg:#e4e4e4;
  --paper:#ffffff;
  --ink:#1e1e1e;
  --text:#555555;
  --white:#ffffff;
  --shadow:rgba(0,0,0,.22);
}
*{margin:0;padding:0;box-sizing:border-box}
html,body{width:1200px;height:1200px;overflow:hidden;background:var(--bg)}
body{position:relative;font-family:"Open Sans",Arial,sans-serif;color:var(--text)}

.sheet{position:absolute;background:var(--paper);box-shadow:0 4px 14px var(--shadow);overflow:hidden}

.brand{font-family:"Montserrat",Arial,sans-serif;font-weight:400;color:var(--ink);text-align:center;line-height:1}
.brand-mark{display:block;margin:0 auto 8px;border:1.5px solid var(--ink)}
.brand-name{display:block;letter-spacing:.06em}
.brand-sub{display:block;letter-spacing:.35em;margin-top:4px}

/* letterhead */
.letterhead{left:118px;top:278px;width:558px;height:716px}
.letterhead .brand{position:absolute;right:66px;top:22px;width:110px}
.letterhead .brand-mark{width:46px;height:46px}
.letterhead .brand-name{font-size:13px}
.letterhead .brand-sub{font-size:6.5px}
.letter-body{position:absolute;left:53px;top:130px;width:450px;font-size:8.6px;line-height:16px}
.letter-meta{line-height:10.5px;margin-bottom:21px}
.letter-date{margin-bottom:10px}
.letter-body p{text-align:justify;margin-bottom:16px}
.salutation{margin-bottom:14px !important}
.closing{margin-top:30px;margin-bottom:4px !important}
.signature{display:block;width:128px;height:14px;background:linear-gradient(90deg,#bdbdbd,#d6d6d6);border-radius:7px;margin-bottom:8px}
.signer{font-size:11px;font-weight:600;color:#333;line-height:14px}
.role{font-size:8.6px}

.footer-band{position:absolute;left:0;right:0;bottom:0;background:var(--ink)}
.letterhead .footer-band{height:100px}
.contact{position:absolute;right:48px;bottom:22px;text-align:right;color:var(--white);font-size:10px;line-height:11px}
.contact li{list-style:none;display:flex;justify-content:flex-end;align-items:center;gap:3px}
.contact .icon{width:8px;height:8px}
.contact .address{margin-top:7px;font-size:10px}

/* envelope front */
.envelope-front{left:715px;top:492px;width:432px;height:217px}
.envelope-front .brand{position:absolute;left:23px;top:16px;width:86px}
.envelope-front .brand-mark{width:37px;height:43px;margin-bottom:7px}
.envelope-front .brand-name{font-size:11px}
.envelope-front .brand-sub{font-size:5.5px}
.envelope-front .footer-band{height:52px}
.envelope-front .address{position:absolute;right:34px;bottom:20px;color:var(--white);font-size:7.4px}

/* envelope back */
.envelope-back{left:717px;top:743px;width:429px;height:213px}
.flap{position:absolute;left:0;top:0;display:block}
.envelope-back .web{position:absolute;left:0;right:0;bottom:29px;text-align:center;font-size:7.4px;color:#333}
</style>
</head>
<body>

<section class="sheet letterhead" aria-label="Letterhead">
  <div class="brand">
    <span class="brand-mark"></span>
    <span class="brand-name">BRIGHTNEST</span>
    <span class="brand-sub">STAYS</span>
  </div>

  <div class="letter-body">
    <p class="letter-meta letter-date">Issuing Date: May 5, 2018</p>
    <p class="letter-meta">Name Of Employee Mr. XYZABC<br>Address of Employee<br>Address Line 2 etc..</p>
    <p class="salutation">Dear Mr.XYZABC</p>
    <p>Lorem Ipsum has been the industry's standard dummy text ever since the 1500s, when an unknown printer took a galley of type and scrambled it to make a type specimen book. It has survived not only five centuries, but also the leap into electronic typesetting, remaining essentially unchanged. It was popularised in the 1960s with the release of Typeleaf sheets containing Lorem Ipsum passages, and more recently with desktop publishing software like Quillset Studio including versions of Lorem Ipsum.</p>
    <p>Lorem Ipsum is simply dummy text of the printing and typesetting industry. Lorem Ipsum has been the industry's standard dummy text ever since the 1500s, when an unknown printer took a galley of type and scrambled it to make a type specimen book.</p>
    <p>It has survived not only five centuries, but also the leap into electronic typesetting, remaining essentially unchanged. It was popularised in the 1960s with the release of Typeleaf sheets containing Lorem IpsumIpsum passages.</p>
    <p class="closing">Yours Sincerely</p>
    <span class="signature" role="img" aria-label="Handwritten signature of Marcus Ellery"></span>
    <div class="signer">Marcus Ellery</div>
    <div class="role">Managing Director</div>
  </div>

  <div class="footer-band" role="img" aria-label="Dark footer band of the letterhead"></div>

  <ul class="contact">
    <li>020-555 318 442
      <svg class="icon" viewBox="0 0 10 10"><path d="M2,1 L4,1 L5,3 L4,4 Q5,6 6,6 L7,5 L9,6 L9,8 Q5,9 2,5 Q1,3 2,1Z" fill="var(--white)"/></svg></li>
    <li>hello@brightnest-mail.com
      <svg class="icon" viewBox="0 0 10 10"><rect x="1" y="2" width="8" height="6" fill="var(--white)"/><path d="M1,2 L5,5.5 L9,2" fill="none" stroke="var(--ink)" stroke-width=".8"/></svg></li>
    <li>www.brightneststays.com
      <svg class="icon" viewBox="0 0 10 10"><circle cx="5" cy="5" r="4" fill="var(--white)"/><path d="M1,5 H9 M5,1 V9" stroke="var(--ink)" stroke-width=".7"/></svg></li>
    <li class="address">88 Harbor Row, Eastport, 20418</li>
  </ul>
</section>

<section class="sheet envelope-front" aria-label="Envelope front">
  <div class="brand">
    <span class="brand-mark"></span>
    <span class="brand-name">BRIGHTNEST</span>
    <span class="brand-sub">STAYS</span>
  </div>
  <div class="footer-band" role="img" aria-label="Dark footer band of the envelope"></div>
  <div class="address">88 Harbor Row, Eastport Quarter, 20418</div>
</section>

<section class="sheet envelope-back" aria-label="Envelope back">
  <svg class="flap" width="429" height="52" viewBox="0 0 429 52" aria-hidden="true">
    <path d="M0,0 H429 L412,50 H18Z" fill="var(--ink)"/>
  </svg>
  <div class="web">www.brightneststays.com</div>
</section>

</body>
</html>
```